winelabels - new design - redesign the existing winelabels

we want to redesign our winelabels, but we want to keep the basic idea of the labels. we want to have a connection to the new label (see sample). Only the basic information should be on the main label, all other informations should be on the side, like in the new label.
restrictions - not wider than 12 cm, the high is fexibel.
we have about 12 different pictures we use for our labels. They have two different highst (see samples). we have two different types of bottles. If you need more information, please give response.
May have a look to our homepage and our shop under www.falkenried-obermaier.de

Reason: there are a lot of very good ideas, but we are still looking for the "perfect" idea

Font styles to use
Other font styles liked:
• for the name "falkenried-obermaier" use the font simelar to the design " Riesling or Muscaris" everthing else is open

Requirements
Must have
• a connection between old an new design

```html
<!DOCTYPE html>
<html lang="de">
<head>
<meta charset="utf-8">
<title>Falkenried-Obermaier – Riesling</title>
<link rel="stylesheet" href="https://fonts.googleapis.com/css2?family=Cormorant+Garamond:wght@500;600&family=Dancing+Script:wght@500&display=swap">
<style>
  :root {
    --page: #ffffff;
    --paper: #f5ede5;
    --paper-edge: #eadfd4;
    --rule: #e2b49b;
    --ink: #4e3020;
    --ink-soft: #7a5438;
    --shell-dark: #5a3a26;
    --shell-light: #c9ab93;
    --pearl: #c98a4e;
  }
  * { margin: 0; padding: 0; box-sizing: border-box; }
  html, body {
    width: 686px; height: 1200px; overflow: hidden;
    background: var(--page);
  }
  .label {
    position: relative;
    width: 686px; height: 1200px;
  }
  .label__frame {
    position: absolute; inset: 0;
    width: 686px; height: 1200px;
  }
  .label__maker {
    position: absolute; top: 228px; left: 0; width: 100%;
    text-align: center;
    font-family: "Cormorant Garamond", Georgia, serif;
    font-weight: 600;
    font-size: 22px;
    letter-spacing: 3px;
    text-transform: uppercase;
    color: var(--ink);
  }
  .label__artwork {
    position: absolute; left: 0; top: 0;
    width: 686px; height: 1200px;
    pointer-events: none;
  }
  .label__name {
    position: absolute; top: 905px; left: 0; width: 100%;
    text-align: center;
    font-family: "Dancing Script", cursive;
    font-weight: 500;
    font-size: 54px;
    color: var(--ink);
  }
  .label__variety {
    position: absolute; top: 1000px; left: 0; width: 100%;
    text-align: center;
    font-family: "Cormorant Garamond", Georgia, serif;
    font-weight: 600;
    font-size: 27px;
    letter-spacing: 1.5px;
    color: var(--ink);
  }
</style>
</head>
<body>
<main class="label">
  <svg class="label__frame" viewBox="0 0 686 1200" aria-hidden="true">
    <defs>
      <radialGradient id="shell-tone" cx="0.5" cy="0.5" r="0.6">
        <stop offset="0" stop-color="var(--shell-dark)"/>
        <stop offset="1" stop-color="var(--shell-light)"/>
      </radialGradient>
      <radialGradient id="pearl-tone" cx="0.4" cy="0.4" r="0.6">
        <stop offset="0" stop-color="#e0b07a"/>
        <stop offset="1" stop-color="var(--pearl)"/>
      </radialGradient>
    </defs>
    <!-- label body with arched crown -->
    <path class="frame-outer" d="M32 1184 V142 Q32 130 44 130 H206 C272 130 312 100 343 36 C374 100 414 130 480 130 H642 Q654 130 654 142 V1184 Z"
          fill="var(--paper)" stroke="var(--paper-edge)" stroke-width="2"/>
    <path class="frame-inner" d="M48 1168 V152 Q48 146 54 146 H210 C276 146 316 118 343 66 C370 118 410 146 476 146 H632 Q638 146 638 152 V1168 Z"
          fill="none" stroke="var(--rule)" stroke-width="1.6"/>

    <!-- crown ornament area -->
    <rect role="img" aria-label="Kleines Zierornament in der Bogenspitze" x="318" y="78" width="50" height="24" rx="12" fill="var(--rule)" opacity="0.55"/>

    <!-- main illustration area -->
    <path role="img" aria-label="Punktierte Illustration eines Ammoniten in Brauntönen"
          d="M170 560 C160 420 250 330 370 330 C470 330 520 400 510 480 C505 560 470 640 440 700 C410 770 400 800 330 815 C250 830 180 720 170 560 Z"
          fill="url(#shell-tone)" opacity="0.85"/>

    <!-- divider with pearl -->
    <line class="divider" x1="105" y1="877" x2="581" y2="877" stroke="var(--ink-soft)" stroke-width="2" stroke-dasharray="1 5" stroke-linecap="round"/>
    <rect role="img" aria-label="Kleines Zierornament links" x="206" y="868" width="28" height="18" rx="9" fill="var(--rule)" opacity="0.6"/>
    <rect role="img" aria-label="Kleines Zierornament rechts" x="452" y="868" width="28" height="18" rx="9" fill="var(--rule)" opacity="0.6"/>
    <circle role="img" aria-label="Kleine Illustration eines Schneckenhauses" cx="343" cy="877" r="28" fill="url(#pearl-tone)"/>
  </svg>

  <p class="label__maker">Falkenried-Obermaier</p>
  <h1 class="label__name">Falkenried-Obermaier</h1>
  <p class="label__variety">RIESLING</p>
</main>
</body>
</html>
```